Web design for Frostwerkly.com

We need a website (4 starter pages) designed for a drupal based site. The theme is flexible so I am open to different designs/looks. I am looking for a VERY simple and clean and FUN design to make it easy to use for the customer.

Our company is similar to Pitch lantern as in it's for multiple people to design a cake for a customer and they choose a winning design and work with that cake designer to make the cake (birthday, wedding etc...)

Our vision:
First page:
2 main images for either the customer to submit an idea for a cake, or the new designer to sign up to the site. Perhaps a mouse-over with wording on what the options are? You can use this site:
http://www.plumwidget.example/ as a sort of template but more clean and simple

"How it works" page:
Similar to this:
http://www.plumwidget.example/how-it-works
Fun, clean and simple

Submit cake design page (form submission)

Submit new designer page

Ideally a 960 wide design with no flash, but open to a flash design if it stands out...

Please contact me if you have any questions!

Target Market(s)

People who want a custom cake made, and people who design and make cakes.

Industry/Entity Type

Wedding

Requirements
Must have
• Use the logo attached. The "Tater Bop" should be a big part of the site...kind of a site mascot?
Nice to have
• 960 wide
No flash but not a deal-breaker if there is flash and it's amazing...

```html
<!DOCTYPE html>
<html lang="en">
<head>
<meta charset="utf-8">
<title>Frostwerkly.com — Hire the Best Bakers</title>
<link rel="stylesheet" href="https://fonts.googleapis.com/css2?family=Lobster&family=Lobster+Two:ital,wght@1,700&family=Ubuntu:wght@300;400;500&family=Open+Sans:ital,wght@0,400;0,600;1,400&display=swap">
<style>
:root{
  --page:#ffffff;
  --pink-light:#fbe3ea;
  --pink:#f6c6d3;
  --pink-card:#fdeef2;
  --pink-border:#f0c3cf;
  --accent:#e0245e;
  --brown:#4a2d12;
  --brown-dark:#3a230c;
  --ribbon:#a8321b;
  --ribbon-dark:#7c2210;
  --gold:#f2cc48;
  --gold-light:#f8e27c;
  --gold-edge:#d9a91e;
  --green:#7bbd1c;
  --green-dark:#5e9a0f;
  --orange:#ef6a23;
  --text:#5a4a44;
  --muted:#8a7a75;
  --footer:#3b3b3b;
  --footer-text:#b9b9b9;
}
*{box-sizing:border-box;margin:0;padding:0}
html,body{width:1116px;height:1200px;overflow:hidden;background:var(--page)}
body{font-family:"Open Sans",sans-serif;color:var(--text);position:relative}
h1,h2{font-weight:400}
.abs{position:absolute}

/* header */
.brand{left:175px;top:30px;display:flex;align-items:center;gap:8px;font-family:"Ubuntu",sans-serif;font-weight:500;font-size:30px;color:var(--brown)}
.brand-mark{width:22px;height:22px;border-radius:50%;background:var(--pink)}
.nav{left:640px;top:42px;display:flex;gap:17px;font-family:"Ubuntu",sans-serif;font-size:12.5px;color:var(--text)}

/* hero */
.hero{left:0;top:76px;width:1116px;height:360px}
.browse{left:187px;top:99px;width:266px;height:298px}
.browse h2{position:absolute;left:0;width:266px;top:16px;text-align:center;font-family:"Ubuntu",sans-serif;font-weight:400;font-size:19px;color:var(--ribbon)}
.browse ul{position:absolute;left:24px;top:72px;width:230px;list-style:none;display:grid;grid-template-columns:110px 120px;row-gap:14px;font-family:"Ubuntu",sans-serif;font-weight:500;font-size:12.5px;color:var(--brown-dark)}
.browse li::before{content:"›";margin-right:7px;font-weight:500}
.mascot-chef{left:585px;top:190px;width:175px;height:240px;border-radius:45% 45% 12% 12%;background:radial-gradient(ellipse at 50% 40%,#f3d2c0 0 35%,#f8e4e8 60%,rgba(255,255,255,0) 74%)}
.mascot-cake{left:744px;top:80px;width:160px;height:200px;border-radius:45% 45% 20% 20%;background:radial-gradient(ellipse at 50% 45%,#f4889f 0 35%,#f6b7c4 58%,rgba(255,255,255,0) 74%)}
.ribbon-title{left:476px;top:108px;z-index:2;font-family:"Lobster",cursive;font-size:31px;color:#fff;white-space:nowrap}
.price{left:485px;top:272px;width:116px;height:116px;border-radius:50% 0 50% 50%;background:radial-gradient(circle at 40% 35%,#e3474f,#c02230);box-shadow:0 3px 6px rgba(0,0,0,.2);color:#fff;text-align:center}
.price .amount{display:block;margin-top:20px;font-family:"Ubuntu",sans-serif;font-weight:500;font-size:44px;line-height:1}
.price .amount sup{font-size:20px;vertical-align:18px}
.price .note{display:block;margin-top:10px;padding-top:6px;border-top:1px solid rgba(255,255,255,.35);font-family:"Ubuntu",sans-serif;font-size:13px;color:#fde2c0}

/* signup */
.headline{left:0;width:1116px;top:448px;text-align:center;font-family:"Lobster Two",cursive;font-style:italic;font-weight:700;font-size:30px;color:var(--brown)}
.signup{left:317px;top:503px;display:flex;align-items:center;height:28px}
.btn-social{width:164px;height:28px;border:1px solid #b9bcc4;border-radius:3px;background:linear-gradient(#f7f8fa,#dfe2e8);display:flex;align-items:center;gap:6px;padding-left:8px;font-family:"Ubuntu",sans-serif;font-size:12.5px;color:#3b5a9a}
.btn-social i{width:14px;height:14px;background:#3b5a9a;border-radius:2px}
.or{margin:0 12px;font-size:11px;color:#3b5a9a}
.email{width:165px;height:28px;border:1px solid #c9c9c9;border-radius:3px;box-shadow:inset 0 1px 2px rgba(0,0,0,.1);padding-left:8px;font-style:italic;font-size:10px;color:#b5b5b5;display:flex;align-items:center}
.btn-go{margin-left:9px;width:103px;height:28px;border-radius:3px;background:linear-gradient(#95d42e,var(--green-dark));color:#203a02;font-family:"Ubuntu",sans-serif;font-size:14px;display:flex;align-items:center;justify-content:center}

/* testimonials */
.section-title{left:150px;top:559px;font-family:"Ubuntu",sans-serif;font-weight:300;font-size:21px;color:var(--muted)}
.quote{top:597px;width:244px;height:131px;background:var(--pink-card);border:1px solid var(--pink-border);border-radius:8px;box-shadow:0 8px 8px -6px rgba(0,0,0,.2)}
.quote .name-bar{position:absolute;left:11px;top:14px;right:-10px;height:38px;background:linear-gradient(var(--brown),var(--brown-dark));color:#fff;font-family:"Ubuntu",sans-serif;font-size:14px;padding-left:70px;display:flex;align-items:center}
.quote .avatar{position:absolute;left:11px;top:14px;width:56px;height:38px;background:linear-gradient(#fff,#f1e3e6);clip-path:polygon(0 0,82% 0,100% 50%,82% 100%,0 100%)}
.quote .avatar span{position:absolute;left:12px;top:4px;width:30px;height:30px;border-radius:50% 50% 10% 10%;background:linear-gradient(#f58bb0 45%,#5b3a22 46%)}
.quote p{position:absolute;left:11px;right:10px;top:61px;font-style:italic;font-size:9.5px;line-height:12px;color:var(--muted)}
.arrow{top:642px;width:26px;height:50px;background:var(--brown-dark);display:flex;align-items:center;justify-content:center}
.arrow.left{left:120px;border-radius:25px 0 0 25px}
.arrow.right{left:970px;border-radius:0 25px 25px 0}

/* contests */
.contests-title{left:155px;top:761px;font-family:"Ubuntu",sans-serif;font-weight:400;font-size:17px;color:var(--text)}
.view-link{font-family:"Ubuntu",sans-serif;font-size:10.5px;color:var(--brown-dark)}
.contests{left:153px;top:789px;width:610px;height:270px;border:1px solid var(--pink-border);border-radius:4px;background:var(--pink-card);overflow:hidden}
.contest{position:relative;height:54px;border-bottom:1px solid var(--pink-border);display:grid;grid-template-columns:374px 119px 92px 25px;align-items:center}
.contest:last-child{border-bottom:0}
.contest .info{padding-left:12px}
.contest .kind{display:block;font-family:"Ubuntu",sans-serif;font-size:9.5px;color:var(--accent);text-transform:uppercase}
.contest .desc{display:block;margin-top:6px;font-style:italic;font-size:9.5px;color:var(--text)}
.contest .time{font-family:"Ubuntu",sans-serif;font-size:13px;color:var(--accent)}
.contest .prize{height:100%;display:flex;align-items:center;justify-content:center;border-left:1px solid var(--pink-border);border-right:1px solid var(--pink-border);font-family:"Ubuntu",sans-serif;font-size:13.5px;color:#222}
.contest .prize small{font-size:9.5px}
.contest .more{writing-mode:vertical-rl;transform:rotate(180deg);justify-self:center;font-family:"Ubuntu",sans-serif;font-size:12px;color:#f1a3b7}

/* bakers */
.bakers-title{left:781px;top:761px;font-family:"Ubuntu",sans-serif;font-weight:400;font-size:19px;color:var(--muted)}
.baker{left:776px;width:190px;height:52px}
.baker .photo{position:absolute;left:0;top:0;width:45px;height:45px;border:1px solid #eee;background:radial-gradient(circle at 50% 45%,#9a4b2a 0 38%,#5a2a12 60%,#fff 62%)}
.baker .name{position:absolute;left:52px;top:-2px;font-family:"Ubuntu",sans-serif;font-size:12px;color:#222}
.baker .stats{position:absolute;left:52px;top:14px;width:138px;height:28px;background:var(--pink-card);padding:2px 0 0 6px;font-size:9.5px;line-height:12px;color:#222}
.baker .stats em{font-style:normal;color:var(--accent)}
.hire{position:absolute;right:0;top:3px;width:52px;height:20px;background:linear-gradient(#f5843a,#e0541a);clip-path:polygon(0 0,88% 0,100% 50%,88% 100%,0 100%);color:#fff;font-family:"Ubuntu",sans-serif;font-size:12px;display:flex;align-items:center;padding-left:8px}

/* press */
.press{left:150px;top:1082px;width:800px;height:44px;display:flex;align-items:center;justify-content:space-between}
.press span{display:block;background:#c9c9c9;border-radius:3px}

/* footer */
.footer{left:0;top:1141px;width:1116px;height:59px;background:var(--footer);color:var(--footer-text);font-size:9px}
.footer .legal{position:absolute;left:177px;top:21px;line-height:12px}
.footer nav{position:absolute;left:546px;top:26px;display:flex;gap:11px;font-family:"Ubuntu",sans-serif;font-size:10.5px;color:#a4a4a4}
</style>
</head>
<body>

<header>
  <div class="abs brand"><span class="brand-mark"></span>Frostwerkly.com</div>
  <nav class="abs nav"><span>How it works</span><span>Login</span><span>Register</span><span>Become a Frostwerkly</span></nav>
</header>

<section>
  <svg class="abs hero" width="1116" height="360" viewBox="0 0 1116 360" aria-hidden="true">
    <defs>
      <linearGradient id="heroFill" x1="0" y1="0" x2="0" y2="1">
        <stop offset="0" stop-color="#f6c2d0"/><stop offset="0.5" stop-color="#fbe0e8"/><stop offset="1" stop-color="#f6c6d3"/>
      </linearGradient>
      <linearGradient id="ribbonFill" x1="0" y1="0" x2="0" y2="1">
        <stop offset="0" stop-color="#b8402a"/><stop offset="1" stop-color="#8a2614"/>
      </linearGradient>
    </defs>
    <path d="M0 0 Q558 18 1116 0 L1116 358 Q558 318 0 358 Z" fill="url(#heroFill)"/>
    <path d="M58 30 L140 27 L140 82 L74 88 L100 58 Z" fill="var(--ribbon-dark)"/>
    <path d="M1058 24 L976 27 L976 82 L1046 88 L1022 56 Z" fill="var(--ribbon-dark)"/>
    <path d="M132 27 Q558 20 984 27 L984 78 Q558 70 132 78 Z" fill="url(#ribbonFill)"/>
  </svg>

  <div class="abs browse">
    <svg width="266" height="298" viewBox="0 0 266 298" style="position:absolute;left:0;top:0" aria-hidden="true">
      <defs>
        <linearGradient id="goldFill" x1="0" y1="0" x2="1" y2="1">
          <stop offset="0" stop-color="var(--gold-light)"/><stop offset="1" stop-color="var(--gold)"/>
        </linearGradient>
      </defs>
      <path d="M0 0 H266 V298 L133 256 L0 298 Z" fill="url(#goldFill)" stroke="var(--gold-edge)" stroke-width="2"/>
      <line x1="40" y1="50" x2="226" y2="50" stroke="var(--gold-edge)" stroke-width="1"/>
    </svg>
    <h2>Browse Tasks</h2>
    <ul>
      <li>Delivery</li><li>Moving Help</li>
      <li>House Chores</li><li>Virtual Assistance</li>
      <li>Shopping</li><li>Event Help</li>
      <li>Office Help</li><li>Skilled</li>
      <li>Handyman</li><li>View full Directory</li>
    </ul>
  </div>

  <div class="abs mascot-chef" role="img" aria-label="Tater Bop mascot: a cartoon chef in a white hat and red scarf"></div>
  <div class="abs mascot-cake" role="img" aria-label="Tall pink layered cake held up by the mascot"></div>
  <div class="abs ribbon-title">Hire the Best Bakers</div>
  <div class="abs price"><span class="amount"><sup>$</sup>99</span><span class="note">*As low As</span></div>
</section>

<section>
  <h1 class="abs headline">Get just about anything done by safe, reliable, awesome people.</h1>
  <div class="abs signup">
    <div class="btn-social"><i></i>Log in with Friendloop</div>
    <span class="or">OR</span>
    <div class="email">Enter E-mail Address</div>
    <div class="btn-go">Get started</div>
  </div>
</section>

<section>
  <h2 class="abs section-title">WHAT DID OUR CUSTOMERS SAY?</h2>
  <div class="abs arrow left"><svg width="10" height="14" viewBox="0 0 10 14"><path d="M9 0 L0 7 L9 14 Z" fill="#fff"/></svg></div>
  <article class="abs quote" style="left:163px">
    <div class="name-bar">Wendell Pike</div>
    <div class="avatar" role="img" aria-label="Pink frosted cupcake"><span></span></div>
    <p>Lorem Ipsum is simply dummy text of the printing and..... typesetting industry. Lorem Ipsum has been the industry's standard dummy text ever since the 1500s,</p>
  </article>
  <article class="abs quote" style="left:432px">
    <div class="name-bar">Corin Hasley</div>
    <div class="avatar" role="img" aria-label="Chocolate topped cupcake"><span></span></div>
    <p>Lorem Ipsum is simply dummy text of the printing and..... typesetting industry. Lorem Ipsum has been the industry's standard dummy text ever since the 1500s.</p>
  </article>
  <article class="abs quote" style="left:703px">
    <div class="name-bar">Brindlevox Co.</div>
    <div class="avatar" role="img" aria-label="Berry cupcake"><span></span></div>
    <p>Lorem Ipsum is simply dummy text of the printing and..... typesetting industry. Lorem Ipsum has been the industry's book. It has survived not only</p>
  </article>
  <div class="abs arrow right"><svg width="10" height="14" viewBox="0 0 10 14"><path d="M1 0 L10 7 L1 14 Z" fill="#fff"/></svg></div>
</section>

<section>
  <h2 class="abs contests-title">Featured Contests</h2>
  <span class="abs view-link" style="left:642px;top:770px">View all Open Contests</span>
  <div class="abs contests">
    <div class="contest"><div class="info"><span class="kind">Wedding Cake</span><span class="desc">Lorem Ipsum is simply dummy text of the printing and typesetting industry.</span></div><span class="time">9 days, 13 hours</span><span class="prize">1000<small>USD</small></span><span class="more">More</span></div>
    <div class="contest"><div class="info"><span class="kind">Mini Iced Cake</span><span class="desc">Lorem Ipsum is simply dummy text of the printing and typesetting</span></div><span class="time">1 day, 15 hours</span><span class="prize">1000<small>USD</small></span><span class="more">More</span></div>
    <div class="contest"><div class="info"><span class="kind">Celebration Cake</span><span class="desc">Lorem Ipsum is simply dummy</span></div><span class="time">6 days, 9 hours</span><span class="prize">400<small>USD</small></span><span class="more">More</span></div>
    <div class="contest"><div class="info"><span class="kind">Wedding Cake</span><span class="desc">Lorem Ipsum is simply dummy text of the</span></div><span class="time">4 days, 9 hours</span><span class="prize">2000<small>USD</small></span><span class="more">More</span></div>
    <div class="contest"><div class="info"><span class="kind">Celebration Cake</span><span class="desc">Lorem Ipsum is simply dummy text of the</span></div><span class="time">3 days, 17 hours</span><span class="prize">223<small>USD</small></span><span class="more">More</span></div>
  </div>

  <h2 class="abs bakers-title">Top Bakers</h2>
  <span class="abs view-link" style="left:925px;top:761px">View all</span>
  <div class="abs baker" style="top:792px"><div class="photo" role="img" aria-label="Chocolate cake"></div><span class="name">Tovrell</span><div class="stats">1129 Entris<br><em>10 Awards</em><span class="hire">Hire</span></div></div>
  <div class="abs baker" style="top:851px"><div class="photo" role="img" aria-label="Strawberry chocolate cake"></div><span class="name">mbquarrin</span><div class="stats">1129 Entris<br><em>08 Awards</em><span class="hire">Hire</span></div></div>
  <div class="abs baker" style="top:909px"><div class="photo" role="img" aria-label="Caramel layer cake"></div><span class="name">Selka</span><div class="stats">800 Entris<br><em>15 Awards</em><span class="hire">Hire</span></div></div>
  <div class="abs baker" style="top:967px"><div class="photo" role="img" aria-label="Dark chocolate torte"></div><span class="name">Ostrid</span><div class="stats">1100 Entris<br><em>20 Awards</em><span class="hire">Hire</span></div></div>
  <div class="abs baker" style="top:1025px"><div class="photo" role="img" aria-label="Red berry cheesecake"></div><span class="name">pelly82</span><div class="stats">900 Entris<br><em>10 Awards</em><span class="hire">Hire</span></div></div>
</section>

<section class="abs press" aria-label="As featured in">
  <span style="width:44px;height:44px;border-radius:50%"></span>
  <span style="width:104px;height:18px"></span>
  <span style="width:152px;height:18px"></span>
  <span style="width:50px;height:36px;border-radius:25px 25px 3px 3px"></span>
  <span style="width:52px;height:32px"></span>
  <span style="width:158px;height:16px"></span>
  <span style="width:82px;height:18px"></span>
</section>

<footer class="abs footer">
  <div class="legal">© 2011-2012 frostwerkly<br>User agreement | Provacy policy | Sitemap</div>
  <nav><span>About</span><span>Menu</span><span>Portions &amp; Prices</span><span>Payment &amp; Delivery</span><span>Our Partners</span><span>Contact</span></nav>
</footer>

</body>
</html>
```